lantern institute of business and technology web site

I need web site for the institute which focus on business courses and computer course it is also for vocation train for employment It is also carear development and advancement .It should have links to online study resource which free
Industry/Entity Type
Business
Number of Pages Required
1 page
Look and feel

```html
<!DOCTYPE html>
<html lang="en">
<head>
<meta charset="utf-8">
<title>Lantern Institute of Business and Technology</title>
<link href="https://fonts.googleapis.com/css2?family=Open+Sans:wght@400;600;700&display=swap" rel="stylesheet">
<style>
  :root {
    --ink: #333333;
    --muted: #6d6d6d;
    --brand: #1e7fc4;
    --brand-dark: #15629a;
    --page: #ececec;
    --card: #ffffff;
    --footer: #2b2b2b;
    --footer-deep: #1d1d1d;
    --footer-text: #a5a5a5;
    --rule: #d7d7d7;
    --photo-warm: #d8cfc3;
    --photo-cool: #c4ccd4;
  }
  * { box-sizing: border-box; margin: 0; padding: 0; }
  html, body { width: 841px; height: 1200px; overflow: hidden; }
  body { font-family: "Open Sans", Arial, sans-serif; color: var(--ink); background: var(--page); position: relative; }

  .site-header { position: absolute; top: 0; left: 0; width: 841px; height: 44px; background: rgba(20,20,20,.92); z-index: 2; }
  .brand { position: absolute; left: 120px; top: 6px; }
  .brand-name { display: inline-block; background: var(--brand); color: #fff; font-weight: 700; font-size: 15px; letter-spacing: 1px; padding: 3px 9px; }
  .brand-tag { display: block; color: #bbb; font-size: 6px; margin-top: 2px; letter-spacing: .3px; }
  .main-nav { position: absolute; right: 60px; top: 16px; display: flex; gap: 20px; }
  .main-nav a { color: #fff; font-size: 8px; font-weight: 600; text-decoration: none; letter-spacing: .3px; }
  .main-nav a.active { color: #7fc1ee; }

  .hero { position: absolute; top: 0; left: 0; width: 841px; height: 420px;
    background: linear-gradient(180deg, #e6e3de 0%, #d6cbbd 60%, #b9ad9e 100%); }
  .hero-dots { position: absolute; left: 50%; top: 398px; transform: translateX(-50%); display: flex; gap: 6px; }
  .hero-dots span { width: 7px; height: 7px; border-radius: 50%; background: rgba(255,255,255,.7); }
  .hero-dots span.on { background: var(--brand); }

  .content { position: absolute; left: 120px; top: 446px; width: 601px; }

  .features { display: flex; gap: 15px; }
  .feature { width: 293px; height: 157px; background: var(--card); position: relative; }
  .feature-photo { height: 115px; background: linear-gradient(180deg, var(--photo-warm), #c6b8a8); }
  .feature-photo.cool { background: linear-gradient(180deg, #d9d4cc, var(--photo-cool)); }
  .feature-bar { position: absolute; bottom: 0; left: 0; right: 0; height: 42px; background: var(--brand); display: flex; align-items: center; padding: 0 12px; color: #fff; }
  .feature-bar svg { margin-right: 8px; }
  .feature-title { font-size: 15px; font-weight: 600; flex: 1; }
  .feature-more { font-size: 8px; }

  .columns { display: flex; gap: 15px; margin-top: 18px; }
  .col { width: 139px; }
  .col h3 { color: var(--brand); font-size: 12px; font-weight: 600; margin-bottom: 4px; }
  .col p { font-size: 7px; color: var(--muted); line-height: 1.45; height: 46px; }
  .col-photo { height: 118px; margin-top: 14px; background: linear-gradient(180deg, #e2dfda, #c9bfb2); }
  .col-photo.cool { background: linear-gradient(180deg, #e0e2e4, #b9c2ca); }

  .about { margin-top: 38px; display: flex; gap: 16px; border-top: 1px solid var(--rule); padding-top: 10px; }
  .about-main { width: 420px; }
  .about-main h2 { color: var(--brand); font-size: 12px; font-weight: 600; margin-bottom: 6px; }
  .about-main p { font-size: 7px; color: var(--muted); line-height: 1.5; margin-bottom: 8px; }
  .about-side { width: 165px; }
  .side-head { display: flex; gap: 8px; }
  .side-thumb { width: 40px; height: 40px; flex: none; background: linear-gradient(180deg, #2f86b8, #1a5d8a); }
  .side-head h4 { color: var(--brand); font-size: 10px; font-weight: 600; line-height: 1.25; }
  .about-side p { font-size: 7px; color: var(--muted); line-height: 1.5; margin-top: 8px; }
  .read-more { display: block; text-align: right; font-size: 7px; color: var(--brand); margin-top: 6px; }

  .site-footer { position: absolute; left: 0; top: 1022px; width: 841px; height: 178px; background: var(--footer); }
  .footer-cols { position: absolute; left: 120px; top: 22px; width: 601px; display: flex; gap: 30px; }
  .footer-col { width: 180px; color: var(--footer-text); font-size: 7px; line-height: 1.7; }
  .footer-col h5 { color: #e5e5e5; font-size: 13px; font-weight: 400; margin-bottom: 10px; }
  .signup { display: flex; margin: 4px 0 6px; }
  .signup span { flex: 1; height: 14px; background: #444; }
  .signup b { width: 24px; height: 14px; background: #5a5a5a; color: #ddd; font-size: 6px; font-weight: 400; display: flex; align-items: center; justify-content: center; }
  .footer-col ul { list-style: none; }
  .footer-col li { border-bottom: 1px solid #3a3a3a; }
  .footer-base { position: absolute; left: 0; bottom: 0; width: 841px; height: 20px; background: var(--footer-deep); color: #777; font-size: 6px; text-align: center; line-height: 20px; }
</style>
</head>
<body>
  <header class="site-header">
    <div class="brand">
      <span class="brand-name">LANTERN</span>
      <span class="brand-tag">institute of business and technology</span>
    </div>
    <nav class="main-nav">
      <a class="active" href="#">HOME PAGE</a>
      <a href="#">ABOUT US</a>
      <a href="#">COURSES</a>
      <a href="#">SERVICES</a>
      <a href="#">PORTFOLIO</a>
      <a href="#">CONTACT US</a>
    </nav>
  </header>

  <section class="hero" role="img" aria-label="Photo: students studying together at desks with books"></section>
  <div class="hero-dots"><span class="on"></span><span></span><span></span></div>

  <main class="content">
    <div class="features">
      <article class="feature">
        <div class="feature-photo" role="img" aria-label="Photo: students working together in a classroom"></div>
        <div class="feature-bar">
          <svg width="18" height="14" viewBox="0 0 18 14"><path d="M9 1 L17 5 L9 9 L1 5 Z" fill="#fff"/><path d="M4 7 V11 Q9 14 14 11 V7" fill="none" stroke="#fff" stroke-width="1.4"/></svg>
          <span class="feature-title">Courses</span><span class="feature-more">See More...</span>
        </div>
      </article>
      <article class="feature">
        <div class="feature-photo cool" role="img" aria-label="Photo: trainees at a group training session"></div>
        <div class="feature-bar">
          <svg width="18" height="14" viewBox="0 0 18 14"><circle cx="6" cy="4" r="3" fill="#fff"/><circle cx="13" cy="4" r="3" fill="#fff"/><path d="M1 13 Q6 6 11 13 Z M8 13 Q13 6 17 13 Z" fill="#fff"/></svg>
          <span class="feature-title">Training</span><span class="feature-more">See More...</span>
        </div>
      </article>
    </div>

    <div class="columns">
      <div class="col"><h3>Business</h3><p>Business and computer courses with practical lessons, guided projects and flexible class times.</p><div class="col-photo" role="img" aria-label="Photo: students in a business class"></div></div>
      <div class="col"><h3>Vocation</h3><p>Vocational training that prepares learners for real jobs and steady employment.</p><div class="col-photo cool" role="img" aria-label="Photo: learners using a laptop"></div></div>
      <div class="col"><h3>Careers</h3><p>Career development support and advice for advancement in every field.</p><div class="col-photo" role="img" aria-label="Photo: student reading in a library"></div></div>
      <div class="col"><h3>Resources</h3><p>Free online study resources open to all of our students at any time.</p><div class="col-photo cool" role="img" aria-label="Photo: group of students on campus"></div></div>
    </div>

    <section class="about">
      <div class="about-main">
        <h2>About Lantern</h2>
        <p>Lantern Institute of Business and Technology offers focused courses in business and computing. Our programmes combine classroom study with hands-on practice so that every learner leaves ready for work. We welcome school leavers, working adults and anyone seeking a new direction in their career.</p>
        <p>Our tutors bring years of industry experience and guide each student through vocational training, job placement and further advancement. Alongside our courses we link to free online study resources, helping learners keep growing long after their final class has ended with us.</p>
      </div>
      <aside class="about-side">
        <div class="side-head">
          <div class="side-thumb" role="img" aria-label="Photo: small campus view"></div>
          <h4>Free study resources for every learner</h4>
        </div>
        <p>Learn new skills with short courses, evening classes and free material online, chosen to match the needs of local employers.</p>
        <a class="read-more" href="#">Continue Reading</a>
      </aside>
    </section>
  </main>

  <footer class="site-footer">
    <div class="footer-cols">
      <div class="footer-col">
        <h5>Stay In The Know !</h5>
        <p>Please enter your email to join our mailing list</p>
        <div class="signup"><span></span><b>GO</b></div>
        <p>Subscribe to news by email</p>
      </div>
      <div class="footer-col">
        <h5>Quick Links !</h5>
        <ul>
          <li>Latest course updates</li>
          <li>Free study resources online</li>
          <li>Career guidance and advice</li>
        </ul>
      </div>
      <div class="footer-col">
        <h5>Company Details !</h5>
        <p>Lantern Institute<br>Business and Technology<br>Student Office<br>Open Weekdays<br>Call our team</p>
      </div>
    </div>
    <div class="footer-base">Copyright &copy; Lantern Institute. All Rights Reserved.</div>
  </footer>
</body>
</html>
```